Finance web application design

We need a design for a new responsive finance web application. It should look uber professional and modern.

Inspiration and design we like:

website:
http://www.brennickhale.com/

The application presented here:
http://markets.pelvantgrid.com/en/products/tools-applications/trading-investment-tools/zarvo-trading-software.html

https://apps.quillstore.example/us/app/ferncastle-for-tablet/id582917463?mt=8

The application presented here (Slatepad version):
https://apps.quillstore.example/en/app/trevik-forex-trading/id649205318?mt=8&utm_source=trevikButton

Target Market(s)

Private Investors

Industry/Entity Type

Finance

Number of Pages Required

5+ page

Font styles to use
Other font styles liked:
• Nobile

Requirements
Must have
• Colors for "up" changes: green
• Colors for "down" changes: red
• Fonts in tables must be very easy to read -
• Deliver design for all pages attached.
Nice to have
• A dark (gray) background
• Graphs should be shaded and partly transparent - orange or blue
• White text as "normal" - orange text / blue text for headers
Should not have
• White background

```html
<!DOCTYPE html>
<html lang="en">
<head>
<meta charset="utf-8">
<title>Home – Open Position</title>
<link rel="stylesheet" href="https://fonts.googleapis.com/css2?family=Roboto:wght@300;400;500&display=swap">
<style>
  :root {
    --page-bg: #eeeeee;
    --screen-bg: #3b3b3d;
    --screen-bg-light: #444446;
    --orange: #ef8a2a;
    --orange-light: #f39a3c;
    --orange-dark: #d9741a;
    --white: #ffffff;
    --ink: #1d1d1d;
    --table-bg: #f1f1f2;
    --table-line: #c9c9cc;
    --table-head-ink: #8d8d92;
  }
  * { box-sizing: border-box; margin: 0; padding: 0; }
  html, body { width: 1200px; height: 1200px; overflow: hidden; }
  body {
    background: var(--page-bg);
    font-family: "Roboto", Arial, sans-serif;
    position: relative;
  }
  .app-screen {
    position: absolute;
    left: 222px; top: 14px;
    width: 756px; height: 1172px;
    background: linear-gradient(160deg, var(--screen-bg) 0%, var(--screen-bg-light) 60%, var(--screen-bg) 100%);
    overflow: hidden;
  }
  .app-header {
    position: absolute; left: 0; top: 0;
    width: 100%; height: 116px;
    background: linear-gradient(180deg, var(--orange-light), var(--orange));
    border-bottom: 4px solid #f6b06a;
  }
  .menu-icon { position: absolute; left: 48px; top: 38px; }
  .header-title {
    position: absolute; left: 0; right: 0; top: 42px;
    text-align: center; color: var(--white);
    font-size: 32px; font-weight: 400; letter-spacing: 0.5px;
  }
  .pin-icon { position: absolute; right: 34px; top: 28px; }

  .tab-bar {
    position: absolute; left: 32px; top: 148px;
    width: 690px; height: 120px;
    background: var(--white);
    border-top: 6px solid var(--orange);
    display: flex; align-items: center; justify-content: space-between;
    padding: 0 20px;
  }
  .tab { font-size: 21px; color: var(--ink); }
  .tab.is-active { color: var(--orange); position: relative; }
  .tab.is-active::after {
    content: ""; position: absolute; left: 50%; bottom: -46px;
    transform: translateX(-50%);
    border: 10px solid transparent; border-bottom-color: var(--screen-bg);
  }

  .section-title {
    position: absolute; left: 0; right: 0; top: 296px;
    text-align: center; color: var(--white);
    font-size: 34px; font-weight: 400;
  }

  .positions-table {
    position: absolute; left: 116px; top: 404px;
    width: 522px;
    border-collapse: collapse;
    background: var(--table-bg);
    border-radius: 6px; overflow: hidden;
    box-shadow: 0 4px 10px rgba(0,0,0,0.35);
  }
  .positions-table th {
    height: 132px; font-weight: 400; font-size: 22px;
    color: var(--table-head-ink); text-align: left; padding-left: 14px;
    border-left: 2px solid var(--table-line);
  }
  .positions-table th.col-name {
    background: linear-gradient(180deg, var(--orange-light), var(--orange-dark));
    color: var(--white); text-align: center; padding: 0;
    width: 216px; border-left: none;
  }
  .positions-table th.col-id { width: 116px; text-align: center; padding: 0; }
  .positions-table th.col-qty { width: 84px; text-align: center; padding: 0; }
  .positions-table td {
    border-top: 2px solid var(--table-line);
    border-left: 2px solid var(--table-line);
    font-size: 16px; color: var(--ink); text-align: center;
  }
  .positions-table td:first-child { border-left: none; font-size: 20px; line-height: 38px; }
  .row-tall td { height: 90px; }
  .row td { height: 46px; }
  .row-empty td { height: 42px; }

  .due-note {
    position: absolute; left: 0; right: 0; top: 836px;
    text-align: center; color: var(--white); font-size: 33px;
  }
  .due-note .due-date { color: var(--orange); }

  .btn-trades {
    position: absolute; left: 270px; top: 920px;
    width: 214px; height: 64px;
    background: var(--white); color: var(--ink);
    border: 2px solid #bdbdbd; font-size: 27px;
    display: flex; align-items: center; justify-content: center;
    font-family: inherit;
  }
</style>
</head>
<body>
  <main class="app-screen">
    <header class="app-header">
      <svg class="menu-icon" width="62" height="42" viewBox="0 0 62 42" aria-label="Menu">
        <g stroke="#ffffff" stroke-width="2.5">
          <line x1="0" y1="2" x2="62" y2="2"/>
          <line x1="0" y1="21" x2="62" y2="21"/>
          <line x1="0" y1="40" x2="62" y2="40"/>
        </g>
      </svg>
      <h1 class="header-title">HOME</h1>
      <svg class="pin-icon" width="38" height="60" viewBox="0 0 38 60" aria-label="Location">
        <path d="M19 57 C10 42 3 32 3 20 A16 16 0 0 1 35 20 C35 32 28 42 19 57 Z" fill="none" stroke="#ffffff" stroke-width="3"/>
        <circle cx="19" cy="19" r="5" fill="#ffffff"/>
      </svg>
    </header>

    <nav class="tab-bar">
      <span class="tab">Dashboard</span>
      <span class="tab is-active">Strategies</span>
      <span class="tab">Portfolios</span>
      <span class="tab">Marketing Data</span>
      <span class="tab">Cust Inst</span>
      <span class="tab">User</span>
    </nav>

    <h2 class="section-title">Open Position</h2>

    <table class="positions-table">
      <thead>
        <tr>
          <th class="col-name">Name</th>
          <th class="col-id">ID</th>
          <th class="col-qty">QTY</th>
          <th class="col-date">Date</th>
        </tr>
      </thead>
      <tbody>
        <tr class="row-tall"><td>Varnex Europe/Real<br>Estate NR USD</td><td>XIUSA04FDF</td><td>145.52</td><td>20.11 12:00</td></tr>
        <tr class="row"><td>Tolvik Marka</td><td>F0GBR04P2S</td><td>142.88</td><td>20.11 12:00</td></tr>
        <tr class="row"><td>VSE VBX Indeks</td><td>XIUSA04GQX</td><td>606.570</td><td>21.11 23:00</td></tr>
        <tr class="row-empty"><td></td><td></td><td></td><td></td></tr>
      </tbody>
    </table>

    <p class="due-note">New Positions is due <span class="due-date">EOD 31.12.2014</span></p>

    <button class="btn-trades" type="button">View All Trades</button>
  </main>
</body>
</html>
```